Business Card Design

I need a card design for Melbourne based business in Australia, called M P Concrete Services. We Concrete and excavate. Concreteing is main part of business.Commercial ,Residential and industrial.We want to be known as M P C (services) as form of abbreviation.We would like to highlight the initials with contact phone. A clean straight edge design. We have no color preference and would prefer a design that can easily be used on all parts of our business including clothing,vechiles and stationary

Industry/Entity Type

Business

Contact Information for Business Card

Hugh 0491 570 156
Peter 0491 570 157
mpcsercices@quollmail.com

```html
<!DOCTYPE html>
<html lang="en">
<head>
<meta charset="utf-8">
<title>M P Concrete Services – Business Card</title>
<link href="https://fonts.googleapis.com/css2?family=Arimo:wght@400&display=swap" rel="stylesheet">
<style>
  :root {
    --card-bg: #f4f5f7;
    --brand-blue: #3a52a4;
    --brand-grey: #818181;
    --ink: #1c1c1c;
  }
  * { margin: 0; padding: 0; box-sizing: border-box; }
  html, body {
    width: 1200px;
    height: 740px;
    overflow: hidden;
    background: var(--card-bg);
  }
  .card {
    position: relative;
    width: 1200px;
    height: 740px;
    background: var(--card-bg);
    font-family: "Arimo", Arial, sans-serif;
  }
  .band-top {
    position: absolute;
    left: 0; top: 8px;
    width: 100%; height: 38px;
    background: var(--brand-blue);
  }
  .band-sub {
    position: absolute;
    left: 0; top: 54px;
    width: 100%; height: 12px;
    background: var(--brand-grey);
  }
  .wordmark {
    position: absolute;
    left: 0; top: 150px;
    width: 1150px;
    text-align: center;
    font-size: 346px;
    font-weight: 400;
    line-height: 1;
    letter-spacing: -14px;
    color: var(--brand-blue);
  }
  .contacts {
    position: absolute;
    left: 0; top: 566px;
    width: 1200px;
    text-align: center;
    font-size: 26px;
    line-height: 44px;
    letter-spacing: 1px;
    color: var(--ink);
  }
  .contact-name { margin-right: 14px; }
  .contact-label { margin-right: 14px; }
</style>
</head>
<body>
  <main class="card">
    <div class="band-top"></div>
    <div class="band-sub"></div>

    <h1 class="wordmark" aria-label="M P C (services)">MPC</h1>

    <section class="contacts">
      <p class="contact-line"><span class="contact-name">Hugh</span><span class="contact-phone">0491 570 156</span></p>
      <p class="contact-line"><span class="contact-name">Peter</span><span class="contact-phone">0491 570 157</span></p>
      <p class="contact-line"><span class="contact-label">E-mail:</span><span class="contact-email">mpcsercices@quollmail.com</span></p>
    </section>
  </main>
</body>
</html>
```